********Quiet Lantern Hawaii Needs A Business Card Design********

We need a logo design for a company based in Hawaii called "Quiet Lantern". We are an audio video "AV" and automation company that does home theaters, lighting and shade control, sound systems, security system, surveillance systems, central vacuum systems, and more. Our company mission is to "Simplify Technology" for our clients. Everything we do aims to make thing simple and reliable for our customers.
The feel of our company is fun, but luxurious. Our colors are red, black, and silver or gray.
The final design of the logo should communicate simplicity, fun, edgy and luxury.
I have included both color versions of our company logo and the shirts that we are looking at making to give you a feel of what we're going for.
I would like our company mission statement to be somewhere on the card and I would like the card to be two sided or I'm open to creative looking cards as well.

I need the following to be on the card somewhere

"Quiet Lantern Hawaii makes living with technology simple and enjoyable by providing reliable, user-friendly systems and the best customer service possible."

Office / Fax: (808) 555-3162
Direct: (808) 555-3162 ext.101
marty@quietlanternhi.example
quietlanternhi.example
Marcus Beddoe

Automation Systems
Lighting & Shade Control
Home Theater Installation & Design
Distributed Audio Video
High Definition Camera Systems
Burglar & Fire Alarms
Central Vacuum

Thank you for your time

Target Market(s)

High End Luxury Market

Industry/Entity Type

Security

Requirements
Must have
• "Quiet Lantern Hawaii makes living with technology simple and enjoyable by providing reliable, user-friendly systems and the best customer service possible."

marty@quietlanternhi.example
quietlanternhi.example
Marcus Beddoe

Automation Systems
Lighting & Shade Control
Distributed Audio Video
Burglar & Fire Alarms
Central Vacuum

```html
<!DOCTYPE html>
<html lang="en">
<head>
<meta charset="utf-8">
<title>Quiet Lantern Hawaii — Business Card</title>
<link rel="stylesheet" href="https://fonts.googleapis.com/css2?family=Titillium+Web:wght@300;400;700&display=swap">
<style>
  :root {
    --backdrop: #b9babd;
    --card-white: #f4f4f4;
    --card-dark: #2a2626;
    --ink: #1e1c1c;
    --ink-soft: #3a3838;
    --red: #c41e2e;
    --silver: #d9d9d9;
    --faint: #e2e2e2;
  }
  * { box-sizing: border-box; margin: 0; padding: 0; }
  html, body { width: 1200px; height: 800px; overflow: hidden; }
  body {
    background: var(--backdrop);
    font-family: "Titillium Web", sans-serif;
    display: flex;
    align-items: center;
    justify-content: center;
    gap: 40px;
  }
  .card {
    position: relative;
    width: 540px;
    height: 310px;
    border-radius: 26px;
    overflow: hidden;
    box-shadow: 0 6px 18px rgba(0,0,0,.25);
  }

  /* Front */
  .card-front { background: var(--card-white); color: var(--ink); }
  .front-band {
    position: absolute; left: 0; right: 0; bottom: 0; height: 14px;
    display: flex;
  }
  .front-band .band-black { width: 32%; background: var(--ink); }
  .front-band .band-red { flex: 1; background: var(--red); }
  .front-ring {
    position: absolute; right: 40px; top: 26px;
    width: 230px; height: 230px;
  }
  .front-brand {
    position: absolute; left: 34px; top: 28px;
    display: flex; flex-direction: column; align-items: flex-start;
  }
  .wordmark {
    display: flex; align-items: center; gap: 10px;
    font-weight: 700; text-transform: uppercase; letter-spacing: .5px; line-height: 1;
  }
  .wordmark .dot {
    width: 22px; height: 22px; border-radius: 50%; background: var(--red);
  }
  .front-brand .wordmark { font-size: 27px; color: var(--ink); }
  .region {
    display: flex; align-items: center; gap: 8px;
    margin-top: 4px; margin-left: 32px;
    font-weight: 400; font-size: 12px; letter-spacing: 6px; text-transform: uppercase;
  }
  .region::before, .region::after {
    content: ""; width: 22px; height: 2px; background: currentColor;
  }
  .person-name {
    position: absolute; left: 34px; top: 104px;
    font-weight: 300; font-size: 24px; color: var(--ink);
  }
  .web-contact {
    position: absolute; left: 34px; top: 152px;
    font-size: 13px; line-height: 1.6; color: var(--red);
  }
  .web-contact .label { color: var(--red); }
  .web-contact .value { color: var(--ink-soft); }
  .mission {
    position: absolute; left: 34px; top: 212px;
    width: 250px;
    font-size: 10.5px; line-height: 1.45; font-style: normal; color: var(--ink-soft);
  }
  .phone-contact {
    position: absolute; right: 34px; bottom: 32px;
    font-size: 14px; line-height: 1.6; text-align: right;
  }
  .phone-contact .label { color: var(--red); }
  .phone-contact .value { color: var(--ink); }

  /* Back */
  .card-back { background: var(--card-dark); color: var(--silver); }
  .services {
    position: absolute; left: 34px; top: 22px;
    list-style: none; font-size: 12.5px; line-height: 1.4; color: var(--silver);
  }
  .services .services-title { color: var(--red); letter-spacing: .5px; }
  .services li.service::before {
    content: "›"; color: var(--red); margin-right: 6px; font-weight: 700;
  }
  .back-brand {
    position: absolute; left: 34px; top: 182px;
    display: flex; flex-direction: column; align-items: flex-start;
  }
  .back-brand .wordmark { font-size: 31px; color: #ffffff; }
  .back-brand .region { color: var(--silver); font-size: 14px; letter-spacing: 8px; margin-left: 40px; }
  .back-web {
    margin-top: 6px; margin-left: 36px;
    font-size: 11px; letter-spacing: 2px; color: #bdbdbd;
  }
  .back-ring {
    position: absolute; right: 26px; top: 70px;
    width: 210px; height: 210px;
  }
</style>
</head>
<body>

  <section class="card card-front" aria-label="Card front">
    <svg class="front-ring" viewBox="0 0 230 230" aria-hidden="true">
      <circle cx="115" cy="115" r="100" fill="none" stroke="var(--faint)" stroke-width="18"/>
    </svg>

    <div class="front-brand">
      <div class="wordmark"><span class="dot"></span>Quiet Lantern</div>
      <div class="region">Hawaii</div>
    </div>

    <p class="person-name">Marcus Beddoe</p>

    <div class="web-contact">
      <p><span class="label">Email:</span> <span class="value">marty@quietlanternhi.example</span></p>
      <p>www.quietlanternhi.example</p>
    </div>

    <p class="mission">Quiet Lantern Hawaii makes living with technology simple and enjoyable by providing reliable, user-friendly systems and the best customer service possible.</p>

    <div class="phone-contact">
      <p><span class="label">Direct:</span> <span class="value">(808) 555-3162 ext.101</span></p>
      <p><span class="label">Office / Fax:</span> <span class="value">(808) 555-3162</span></p>
    </div>

    <div class="front-band"><span class="band-black"></span><span class="band-red"></span></div>
  </section>

  <section class="card card-back" aria-label="Card back">
    <ul class="services">
      <li class="services-title">SERVICES:</li>
      <li class="service">Automation Systems</li>
      <li class="service">Lighting &amp; Shade Control</li>
      <li class="service">Home Theater Installation &amp; Design</li>
      <li class="service">Distributed Audio Video</li>
      <li class="service">High Definition Camera Systems</li>
      <li class="service">Burglar &amp; Fire Alarms</li>
      <li class="service">Central Vacuum</li>
    </ul>

    <div class="back-brand">
      <div class="wordmark">Quiet Lantern</div>
      <div class="region">Hawaii</div>
      <p class="back-web">www.quietlanternhi.example</p>
    </div>

    <svg class="back-ring" viewBox="0 0 210 210" aria-hidden="true">
      <circle cx="105" cy="105" r="92" fill="none" stroke="#e8e8e8" stroke-width="16"/>
    </svg>
  </section>

</body>
</html>
```